Kettlebloomreads: Self-help book needs Promotional Postcard

Need a postcard 8.5" x 5.5" to promote my upcoming book. Its a self-help career book for women focusing on how the mother-daughter relationship impacts careers and tips and solutions for success. The model includes 5 different types of daughters.
Title: Where Did the Old Lantern Go Tonight?
Breathe new life into your career by understanding your mother daughter relationship.
Book release is January 9, 2017
Updates

I just uploaded 5 images of the daughter types without the words, better to use these, thanks! Added Thursday, December 29, 2016

Target Market(s)

This book is targeted towards women

Industry/Entity Type

Promotional

Font styles to use
Serif
Other font styles liked:
• see website text

Colors
00a990
ec252d
e34297

Requirements
Must have
• Eye catching promotional postcard. Must have image of book on front with title and subtitle, author name and website. I'd like images of the 5 daughters on the front.
• Colors should match the cover green and pink
• Back can have quotes and author bio
• can look at website (not quite completed) for more inspiration www.kettlebloomreads-example.com
Nice to have
• Curious to see how the postcard compliments the book and website.

```html
<!DOCTYPE html>
<html lang="en">
<head>
<meta charset="utf-8">
<title>Kettlebloomreads – Promotional Postcard</title>
<link rel="stylesheet" href="https://fonts.googleapis.com/css2?family=Antonio:wght@300;400&family=Montserrat:wght@500;700&family=Raleway:ital,wght@0,400;0,500;0,700;1,400&display=swap">
<style>
:root{
  --sage:#87996a;
  --sage-light:#93a476;
  --sage-dark:#7b8d5f;
  --book-face:#9aab7c;
  --book-edge:#f1f1ea;
  --olive:#343a25;
  --pink:#d8285f;
  --ink:#2c2f25;
  --paper:#ffffff;
  --text-light:#f4f5ee;
}
*{margin:0;padding:0;box-sizing:border-box}
html,body{width:1200px;height:1200px;overflow:hidden;background:var(--paper)}
body{position:relative;font-family:"Raleway",sans-serif;color:var(--ink)}
.card{position:absolute;left:163px;width:874px;overflow:hidden;
  background:radial-gradient(ellipse at 40% 40%,var(--sage-light),var(--sage) 60%,var(--sage-dark))}
.card-front{top:28px;height:566px}
.card-back{top:604px;height:566px}
.accent-band{position:absolute;left:0;bottom:0;width:100%;height:10px;background:var(--pink);z-index:3}

.author-line{position:absolute;left:0;width:520px;top:54px;text-align:center;
  font-family:"Montserrat",sans-serif;font-weight:500;font-size:20px;color:#2f3326;white-space:nowrap}
.book-title{position:absolute;left:0;width:520px;top:96px;text-align:center;
  font-family:"Antonio",sans-serif;font-weight:300;font-size:64px;line-height:74px;
  color:var(--pink);text-transform:uppercase}
.tagline{position:absolute;left:10px;width:500px;top:332px;text-align:center;
  font-size:18px;line-height:24px;color:#2f3326;white-space:nowrap}
.site-button{position:absolute;left:106px;top:402px;width:310px;height:30px;
  border:1.5px solid #4d5540;border-radius:5px;display:flex;align-items:center;gap:6px;padding-left:10px;
  font-size:13.5px;color:var(--pink);white-space:nowrap}
.site-button svg{flex:none}
.book-mockup{position:absolute;left:500px;top:20px;width:345px;height:520px;z-index:1}
.daughter-row{position:absolute;left:25px;top:452px;width:540px;height:114px;display:flex;gap:22px;z-index:2}
.daughter{flex:1;background:linear-gradient(180deg,#f2f2ee 0%,#e6e6e0 40%,#111 75%);border-radius:50% 50% 6px 6px}

.intro{position:absolute;left:49px;top:40px;width:760px;font-size:15.5px;line-height:21px;color:var(--text-light)}
.quotes{position:absolute;left:53px;top:150px;width:758px;column-count:2;column-gap:32px;
  font-size:12.2px;line-height:16.4px;color:#2f3326}
.quote{margin-bottom:9px}
.quote cite{display:block;font-style:normal;font-size:10.6px;line-height:14.4px;margin-top:4px}
.quote cite b{font-weight:700}
.quote cite i{font-style:italic}
.quote em{color:var(--pink);font-style:italic}

.author-panel{position:absolute;left:0;top:348px;width:100%;height:218px;background:var(--olive);color:var(--text-light)}
.author-photo{position:absolute;left:47px;top:4px;width:120px;height:148px;border:2px solid #c9ccbf;border-radius:10px;
  background:linear-gradient(160deg,#5f7042,#3e4a2a)}
.author-name{position:absolute;left:47px;top:165px;font-size:12px;font-weight:700;white-space:nowrap}
.bio{position:absolute;left:189px;top:34px;width:640px;font-size:13.8px;line-height:19px}
.social{position:absolute;left:200px;top:156px;display:flex;align-items:center;gap:10px}
.social span{width:18px;height:18px;border-radius:50%;background:var(--text-light)}
.social i{width:1px;height:20px;background:#8f927f}
.booking{position:absolute;left:318px;top:146px;font-size:14px;line-height:18px}
.booking b{font-weight:700}
</style>
</head>
<body>

<section class="card card-front">
  <p class="author-line">Maren Holloway Castell, M.A, M.ed</p>
  <h1 class="book-title">Where Did the<br>Old Lantern<br>Go Tonight?</h1>
  <p class="tagline">Breathe new life into your career by<br>understanding your mother daughter relationship.</p>
  <div class="site-button">
    <svg width="16" height="20" viewBox="0 0 16 20"><path d="M5 2v9l-2-2c-1-1-2.5 0-1.7 1.2L5 16c1 2 2.5 3 5 3 3 0 4.5-2 4.5-5V9c0-1.2-1.5-1.2-1.8 0V8c0-1.2-1.6-1.2-1.8 0V7.5c0-1.2-1.7-1.2-1.8 0V2c0-1.3-2.1-1.3-2.1 0z" fill="#fff" stroke="#333" stroke-width="1"/></svg>
    www.kettlebloomreads-example.com
  </div>
  <svg class="book-mockup" viewBox="0 0 345 520" role="img" aria-label="Book cover shown in perspective with title, subtitle and author name">
    <polygon points="13,48 333,8 333,28 16,68" fill="var(--book-edge)"/>
    <polygon points="16,68 333,28 329,424 61,500" fill="var(--book-face)" style="filter:drop-shadow(10px 14px 14px rgba(0,0,0,.3))"/>
  </svg>
  <div class="daughter-row">
    <div class="daughter" role="img" aria-label="Silhouette illustration of daughter type one"></div>
    <div class="daughter" role="img" aria-label="Silhouette illustration of daughter type two"></div>
    <div class="daughter" role="img" aria-label="Silhouette illustration of daughter type three"></div>
    <div class="daughter" role="img" aria-label="Silhouette illustration of daughter type four"></div>
    <div class="daughter" role="img" aria-label="Silhouette illustration of daughter type five"></div>
  </div>
  <div class="accent-band"></div>
</section>

<section class="card card-back">
  <p class="intro">Are you unhappy at work? Feeling uncertain about your career choices in general? Your relationship with your mother might be the last thing on your mind as a major contributing factor to your career woes but it shouldn't be. Unlock the mystery to the patterns and choices you make throughout your career. Read about the five daughter types, and learn how to propel your career forward.</p>

  <div class="quotes">
    <blockquote class="quote">“...Maren draws the reader in with her poignant and insightful perspective of how family dynamics, particularly the conscious and subconscious aspects of the mother/daughter relationship, impact a career path and a fulfilled life...”
      <cite><b>Judge Renata Vollmer,</b> <i>OPEN DOCKET, a syndicated TV court program.</i></cite></blockquote>
    <blockquote class="quote">“...Putting the not so obvious 2 + 2 together (mothers + careers) gives all women a chance to stand up in their own truth, letting go of old messages (conscious and unconscious) that still define them, even in the workplace... a great "how to" book, with tips that will serve you well, no matter which daughter type you might be...”
      <cite><b>Dr. Celia Brannock,</b> co-author with her mother of Kin &amp; Keepers: Finding Common Ground and other books including: Warm Bread for the Mother &amp; Daughter Heart..</cite></blockquote>
    <blockquote class="quote">“...'<em>Old Lantern</em>' challenges us to pay attention to how we show up at work without assigning blame or judgement. Maren draws on decades of career counseling to provide knowledgeable insight and practical tips, wrapped in a warm hug...”
      <cite><b>Noreen P Aldous,</b> Executive Women's Leadership and Mindfulness Coach.</cite></blockquote>
  </div>

  <div class="author-panel">
    <div class="author-photo" role="img" aria-label="Portrait photograph of the author"></div>
    <p class="author-name">Maren Holloway Castell</p>
    <p class="bio">Maren Holloway Castell, M.A., M.Ed. is a clinical career counselor and licensed mental health counselor who has been helping clients make meaningful career transitions and address workplace challenges for over 26 years. She is the 2013 recipient of the Outstanding Career Practitioner Award from the Allied Career Guidance Society. 'Old Lantern' integrates her expertise in career development with her training and insight about the adult mother-daughter relationship.</p>
    <div class="social"><span></span><i></i><span></span><i></i><span></span></div>
    <p class="booking">To Book Maren for a speaking event, please contact her at <b>555 014-2287</b> or<br>visit <b>www.kettlebloomreads-example.com</b> for more information.</p>
  </div>
  <div class="accent-band"></div>
</section>

</body>
</html>
```